Mechanical Contractor Business Card and Stationary Design
VoltaCrest Mechanical LLC
Use same font as used in my logo
Helvetica Neue
Simple
Marcus T. Holloway, PE, LEED AP
Managing Member
512-867-0ZAP
mholloway@voltacrestmechanical.com
www.voltacrestmechanical.com
TACLA000048153B
We would like the stationary and business cards to be clean and crisp like the logo. Colors that are applicable are those used in the logo as well as blue and red. The ideal winner will have a catchy and memorable design, while respecting the white space and maintaining a design consistent with the logo.
Logo Font: Helvetica Neue
please message me or contact me with questions.

```html
<!DOCTYPE html>
<html lang="en">
<head>
<meta charset="utf-8">
<title>VoltaCrest Mechanical — Business Card</title>
<link href="https://fonts.googleapis.com/css2?family=Arimo:wght@400;700&display=swap" rel="stylesheet">
<style>
  :root {
    --stage: #e6e7e8;
    --card-white: #ffffff;
    --card-dark: #3b3c3e;
    --silver-light: #f4f4f4;
    --silver-mid: #d9dadb;
    --brand-green: #5aa21f;
    --brand-green-light: #7cc243;
    --charcoal: #555659;
    --ink: #4a4a4c;
    --muted: #77787b;
  }
  * { margin: 0; padding: 0; box-sizing: border-box; }
  html, body { width: 1200px; height: 901px; overflow: hidden; }
  body {
    background: var(--stage);
    font-family: "Arimo", "Helvetica Neue", Arial, sans-serif;
    display: flex;
    align-items: center;
    justify-content: center;
    gap: 40px;
  }
  .card {
    width: 540px;
    height: 309px;
    border-radius: 18px;
    position: relative;
    overflow: hidden;
    box-shadow: 0 6px 18px rgba(0,0,0,0.18);
  }
  .card svg.bands { position: absolute; inset: 0; }

  /* Brand name */
  .brand {
    position: absolute;
    display: flex;
    align-items: center;
    gap: 10px;
    font-weight: 700;
    color: var(--charcoal);
    letter-spacing: -0.5px;
  }
  .brand-mark {
    width: 22px; height: 22px;
    background: var(--brand-green);
  }

  /* Front */
  .card-front { background: var(--card-white); }
  .card-front .brand { left: 150px; top: 58px; font-size: 30px; }
  .person {
    position: absolute;
    right: 28px;
    top: 138px;
    font-size: 15px;
    color: var(--brand-green);
  }
  .website {
    position: absolute;
    right: 28px;
    top: 168px;
    font-size: 13px;
    color: #ffffff;
    letter-spacing: 0.3px;
  }
  .role {
    position: absolute;
    right: 28px;
    top: 192px;
    font-size: 12px;
    color: var(--muted);
  }
  .address {
    position: absolute;
    left: 26px;
    top: 222px;
    font-size: 12.5px;
    line-height: 1.45;
    color: var(--ink);
  }
  .divider {
    position: absolute;
    left: 252px;
    top: 222px;
    width: 1px;
    height: 58px;
    background: var(--muted);
  }
  .contacts {
    position: absolute;
    left: 266px;
    top: 220px;
    list-style: none;
    font-size: 12.5px;
    line-height: 1.48;
    color: var(--ink);
  }
  .contacts li { display: flex; align-items: center; gap: 8px; }
  .contacts svg { width: 12px; height: 12px; flex: none; }

  /* Back */
  .card-back { background: var(--card-dark); }
  .card-back .brand { left: 145px; top: 178px; font-size: 32px; }
</style>
</head>
<body>

  <section class="card card-front" aria-label="Business card front">
    <svg class="bands" width="540" height="309" viewBox="0 0 540 309" aria-hidden="true">
      <polygon points="0,148 165,148 178,162 0,162" fill="var(--charcoal)"/>
      <polygon points="183,162 540,162 540,186 205,186" fill="var(--brand-green)"/>
      <rect x="0" y="186" width="540" height="2" fill="var(--brand-green-light)"/>
    </svg>

    <div class="brand"><span class="brand-mark"></span>VoltaCrest Mechanical</div>

    <p class="person">Marcus T. Holloway, PE, LEED AP</p>
    <p class="website">www.voltacrestmechanical.com</p>
    <p class="role">Managing Member</p>

    <p class="address">
      VoltaCrest Mechanical, LLC<br>
      4820 Ridgeline Blvd, Suite 210<br>
      Austin, Texas 78731
    </p>
    <div class="divider"></div>
    <ul class="contacts">
      <li>
        <svg viewBox="0 0 12 12"><path d="M2 1h3l1 3-1.5 1a6 6 0 0 0 2.5 2.5L8 6l3 1v3a1 1 0 0 1-1 1A9 9 0 0 1 1 2a1 1 0 0 1 1-1z" fill="var(--muted)"/></svg>
        512-867-0ZAP
      </li>
      <li>
        <svg viewBox="0 0 12 12"><rect x="3" y="0.5" width="6" height="11" rx="1" fill="var(--muted)"/><rect x="4" y="2" width="4" height="6" fill="#fff"/></svg>
        512-555-0147
      </li>
      <li>
        <svg viewBox="0 0 12 12"><rect x="0.5" y="2" width="11" height="8" fill="var(--muted)"/><path d="M1 2.5l5 4 5-4" stroke="#fff" stroke-width="1" fill="none"/></svg>
        mholloway@voltacrestmechanical.com
      </li>
    </ul>
  </section>

  <section class="card card-back" aria-label="Business card back">
    <svg class="bands" width="540" height="309" viewBox="0 0 540 309" aria-hidden="true">
      <defs>
        <linearGradient id="silver" x1="0" y1="0" x2="0" y2="1">
          <stop offset="0" stop-color="var(--silver-light)"/>
          <stop offset="1" stop-color="var(--silver-mid)"/>
        </linearGradient>
      </defs>
      <rect x="0" y="160" width="540" height="72" fill="url(#silver)"/>
    </svg>
    <div class="brand"><span class="brand-mark"></span>VoltaCrest Mechanical</div>
  </section>

</body>
</html>
```